Law Firm Website, easily updated by User

We are a regional Labor and Employment Law Firm with a tired outdated website. We are looking for a clean easy to use website that will allow us to easily update information and articles in house. Our current website can be found at www.quillbarrowfirm.com

Industry/Entity Type

Labor

Number of Pages Required

5+ page

Colors
0655a3

Requirements
Must have
• Content easily updated by user
Nice to have
• crisp clean pages
Should not have
• stock pictures

```html
<!DOCTYPE html>
<html lang="en">
<head>
<meta charset="utf-8">
<title>Quillbarrow &amp; Associates, P.C.</title>
<link rel="stylesheet" href="https://fonts.googleapis.com/css2?family=Open+Sans:wght@400;600&family=Tinos:wght@400&family=Arimo:wght@400&display=swap">
<style>
  :root {
    --brand-blue: #0655a3;
    --navy: #1c2f6b;
    --ink: #222222;
    --nav-grey: #6b6b6b;
    --accent-green: #4a9a2a;
    --white: #ffffff;
    --stone-dark: #3e4043;
    --stone-mid: #6f7173;
  }
  * { margin: 0; padding: 0; box-sizing: border-box; }
  html, body { width: 1200px; height: 733px; overflow: hidden; background: var(--white); }
  body { position: relative; font-family: "Open Sans", sans-serif; }

  .site-header { position: absolute; left: 0; top: 0; width: 1200px; height: 129px; background: var(--white); }
  .brand { position: absolute; left: 115px; top: 16px; }
  .brand-name {
    font-family: "Tinos", serif; font-size: 25px; color: var(--ink);
    line-height: 1; display: flex; align-items: center; gap: 8px;
  }
  .brand-mark { width: 12px; height: 12px; background: var(--navy); display: inline-block; }
  .brand-tagline {
    margin-top: 6px; border-top: 2px solid var(--ink); padding-top: 3px;
    font-family: "Tinos", serif; font-size: 8px; letter-spacing: 0.2px; color: var(--ink);
  }

  .main-nav { position: absolute; right: 155px; top: 88px; display: flex; gap: 25px; }
  .main-nav a {
    font-size: 13.5px; color: var(--nav-grey); text-decoration: none;
    padding-bottom: 3px; border-bottom: 2px solid var(--brand-blue); line-height: 1.2;
  }
  .main-nav a.is-active { color: var(--ink); }

  .hero { position: absolute; left: 0; top: 129px; width: 1200px; height: 604px; overflow: hidden; }
  .hero-photo {
    position: absolute; inset: 0;
    background: linear-gradient(100deg, var(--stone-dark) 0%, var(--stone-mid) 35%, #8d8f91 55%, var(--stone-mid) 75%, var(--stone-dark) 100%);
  }
  .consult-cta {
    position: absolute; left: 780px; top: 20px; width: 265px; height: 30px;
    background: var(--brand-blue); color: var(--white);
    font-family: "Arimo", sans-serif; font-size: 13.5px;
    display: flex; align-items: center; justify-content: center;
  }
  .slide-title {
    position: absolute; left: 111px; top: 264px; width: 510px;
    border-top: 2px solid var(--white); border-bottom: 1px solid var(--white);
    color: var(--white); font-size: 44px; line-height: 74px; font-weight: 400;
    white-space: nowrap;
  }
  .slider-controls { position: absolute; left: 967px; top: 321px; display: flex; gap: 1px; }
  .slider-controls span {
    width: 38px; height: 38px; border: 1px solid var(--white);
    display: flex; align-items: center; justify-content: center;
  }

  .admissions-card {
    position: absolute; left: 111px; top: 437px; width: 311px; height: 180px;
    background: var(--white); padding: 22px 29px;
  }
  .admissions-card h2 { font-size: 23px; font-weight: 400; color: var(--accent-green); line-height: 1.2; margin-bottom: 14px; }
  .admissions-card p { font-family: "Arimo", sans-serif; font-size: 12.5px; line-height: 18.5px; color: var(--ink); }
</style>
</head>
<body>
  <header class="site-header">
    <div class="brand">
      <div class="brand-name"><span class="brand-mark"></span>Quillbarrow &amp; Associates, P.C.</div>
      <div class="brand-tagline">EMPLOYMENT COUNSELING, LITIGATION, LABOR &amp; BENEFITS LAW</div>
    </div>
    <nav class="main-nav">
      <a class="is-active" href="#">Main</a>
      <a href="#">Contact Us</a>
      <a href="#">Attorneys</a>
      <a href="#">Practice Areas</a>
      <a href="#">FAQ</a>
      <a href="#">In The News</a>
      <a href="#">For Employers</a>
    </nav>
  </header>

  <section class="hero">
    <div class="hero-photo" role="img" aria-label="Close-up of brushed steel lettering reading Law Court on a dark granite wall"></div>
    <div class="consult-cta">For a Free Consultation Call (555) 214-0386</div>
    <h1 class="slide-title">Employment Counseling</h1>
    <div class="slider-controls">
      <span><svg width="12" height="22" viewBox="0 0 12 22"><polyline points="11,1 1,11 11,21" fill="none" stroke="#ffffff" stroke-width="1"/></svg></span>
      <span><svg width="12" height="22" viewBox="0 0 12 22"><polyline points="1,1 11,11 1,21" fill="none" stroke="#ffffff" stroke-width="1"/></svg></span>
    </div>
    <div class="admissions-card">
      <h2>Admissions</h2>
      <p>New York State / Eastern District of New York / Southern District of New York / United States Court of Appeals for the Second Circuit / United States Court of Federal Claims / United States Supreme Court</p>
    </div>
  </section>
</body>
</html>
```